Company Brochure / Data Sheet Template Design

We need a brochure / data sheet template for a new company based in Texas focused on Information Technology consulting. The design should instill professionalism, confidence, and strength. The company name is Brightwell Systems Partners, so you can incorporate alchemy concept into the design. I have attached the logo for the company. Our customers are medium and large businesses. We would like the top bar to incorporate black background to complement the black logo. Alternatively, you can incorporate the blue color and the white logo.

We will use this template for all corporate market materials. It should be usable for 1-6 pages documents.

Below are a couple examples by large technology companies:
http://www.korvanta.com/files/pdf/products/nimbrel/Korvanta-Nimbrel-zRAQ-Pricing-FAQs.pdf
https://www.peltrox.com/content/dam/peltrox/en_us/documents/products-solutions/the-peltrox-advantage-for-quillos-10.pdf

Please let us know if you have any questions.

Target Market(s)

Large Corporations and Small-to-Medium sized businesses

Industry/Entity Type

Information Technology

Font styles to use
Other font styles liked:
• Copperplate Gothic or something similar to the logo design

Requirements
Must have
• Design on the top of the page cover cross the entire page. Incorporate www.brightwellsyspartners.com or logo at the bottom of the page. Incorporate page numbers at the bottom of the page. Template should have the ability to incorporate 1 or 2 columns of content.
• This should match the look and feel of the logo.
Nice to have
• Template should have the ability to incorporate 1 or 2 columns of content
• Incorporate font and blue color into the design.
• Blue color could be incorporated into the headings of the content
Should not have
• This needs to be professional, not playful.

```html
<!DOCTYPE html>
<html lang="en">
<head>
<meta charset="utf-8">
<title>Brightwell Systems Partners — Data Sheet</title>
<link rel="stylesheet" href="https://fonts.googleapis.com/css2?family=Cinzel:wght@400&family=Roboto:wght@300;400;700&family=Roboto+Condensed:wght@300;400;700&display=swap">
<style>
  :root{
    --ink:#000;
    --panel:#0b0d0f;
    --teal:#2aa3bd;
    --teal-deep:#1f7f92;
    --paper:#fff;
    --text:#111;
    --muted:#8a8f93;
  }
  *{margin:0;padding:0;box-sizing:border-box}
  html,body{width:919px;height:1200px;overflow:hidden;background:var(--paper)}
  .page{position:relative;width:919px;height:1200px;overflow:hidden;background:var(--paper);font-family:"Roboto Condensed",Arial,sans-serif;color:var(--text)}

  /* Header */
  .masthead{position:absolute;left:0;top:0;width:919px;height:143px;background:var(--ink)}
  .masthead__name{position:absolute;left:72px;top:54px;font-family:"Cinzel",serif;font-size:24px;color:var(--teal);letter-spacing:.5px}
  .masthead__stripes{position:absolute;left:0;top:0}
  .brand-mark{position:absolute;display:flex;align-items:center;gap:10px;color:#e6e6e6;font-family:"Roboto",Arial,sans-serif;font-weight:300;letter-spacing:2px;text-transform:uppercase}
  .brand-mark__square{width:14px;height:14px;background:var(--teal);flex:none}
  .brand-mark--header{left:724px;top:52px;font-size:17px;line-height:1.3}
  .rule-white{position:absolute;left:0;top:143px;width:919px;height:4px;background:var(--paper)}
  .rule-black{position:absolute;left:0;top:147px;width:919px;height:6px;background:var(--ink)}

  /* Sidebar */
  .sidebar{position:absolute;left:0;top:158px;width:240px;height:1042px;background:linear-gradient(180deg,#080a0c 0%,#111417 45%,#090b0d 100%)}
  .sidebar__pixels{position:absolute;left:10px;top:0;width:230px;height:125px;background:linear-gradient(160deg,rgba(42,163,189,.38),rgba(42,163,189,.05) 80%)}
  .sidebar__drawing{position:absolute;left:0;top:330px;width:240px;height:680px;background:radial-gradient(ellipse at 40% 40%,rgba(255,255,255,.05),rgba(255,255,255,0) 70%)}
  .brand-mark--side{left:28px;top:272px;font-size:18px;line-height:1.3;color:#c9c9c9}
  .sidebar__url{position:absolute;left:44px;top:1003px;font-size:14px;color:var(--muted);letter-spacing:-.3px}

  /* Content */
  .content{position:absolute;left:256px;top:178px;width:654px}
  .title{font-family:"Roboto",Arial,sans-serif;font-weight:700;font-size:29px;letter-spacing:-.4px;line-height:36px}
  .lead{margin-top:10px;font-family:"Roboto Condensed",Arial,sans-serif;font-weight:300;font-size:22px;line-height:27.2px;color:var(--teal);text-align:justify;letter-spacing:-.6px}

  .stats{position:absolute;left:240px;top:376px;width:679px;height:178px;background:var(--ink)}
  .stat{position:absolute;top:13px;width:140px;text-align:center}
  .stat svg{display:block;margin:0 auto}
  .stat__value{position:absolute;left:0;top:50px;width:140px;font-family:"Roboto",Arial,sans-serif;font-weight:700;font-size:16px;color:var(--teal)}
  .stat__label{margin-top:9px;font-family:"Roboto",Arial,sans-serif;font-size:12px;color:#e8e8e8}

  .article{position:absolute;left:256px;top:566px;width:654px}
  .article__title{font-family:"Roboto",Arial,sans-serif;font-weight:300;font-size:22px;letter-spacing:-.4px;line-height:30px}
  .article__sub{margin-top:9px;font-family:"Roboto",Arial,sans-serif;font-weight:700;font-size:15px;color:var(--teal);line-height:18px}
  .article p{font-size:14px;line-height:27.2px;text-align:justify;letter-spacing:-.45px;margin-top:-2px}
  .article__conclusion{margin-top:8px;font-family:"Roboto",Arial,sans-serif;font-weight:300;font-size:21px;line-height:24px;letter-spacing:-.3px}
  .read-more a{color:var(--teal);text-decoration:none}

  .page-tag{position:absolute;right:0;top:1156px;height:30px;padding:0 24px 0 14px;background:var(--ink);color:var(--teal);font-size:15px;line-height:30px;letter-spacing:-.3px}
</style>
</head>
<body>
<div class="page">

  <header class="masthead">
    <div class="masthead__name">Brightwell Systems Partners</div>
    <svg class="masthead__stripes" width="919" height="143" viewBox="0 0 919 143" aria-hidden="true">
      <polygon points="653,0 681,0 601,143 573,143" fill="#fff"/>
      <polygon points="692,0 731,0 651,143 612,143" fill="#fff"/>
    </svg>
    <div class="brand-mark brand-mark--header">
      <span class="brand-mark__square"></span>
      <span>Brightwell<br>Systems Partners</span>
    </div>
  </header>
  <div class="rule-white"></div>
  <div class="rule-black"></div>

  <aside class="sidebar">
    <div class="sidebar__pixels" role="img" aria-label="Scattered teal pixel squares decoration"></div>
    <div class="sidebar__drawing" role="img" aria-label="Faint technical drawing texture"></div>
    <div class="brand-mark brand-mark--side">
      <span class="brand-mark__square"></span>
      <span>Brightwell<br>Systems Partners</span>
    </div>
    <div class="sidebar__url">www.brightwellsyspartners.com</div>
  </aside>

  <section class="content">
    <h1 class="title">Technology and the Future of Digital Marketing</h1>
    <p class="lead">Lorem ipsum dolor sit amet, consectetur adipiscing elit. Curabitur fringilla vehicula massa, ac lacinia arcu semper vitae. Nunc elementum mi nec ullamcorper pretium. Nulla id faucibus risus. Aenean varius ante eget bibendum lacinia. Aenean lobortis facilisis aliquet. Nullam aliquet turpis diam, a sodales turpis euismod sit amet. Proin magna leo ielit.</p>
  </section>

  <section class="stats">
    <div class="stat" style="left:28px">
      <svg width="130" height="130" viewBox="0 0 130 130" aria-hidden="true">
        <circle cx="65" cy="65" r="60" fill="none" stroke="var(--teal)" stroke-width="5" stroke-dasharray="237.5 377" transform="rotate(-90 65 65)"/>
      </svg>
      <div class="stat__value">63%</div>
      <div class="stat__label">Prima</div>
    </div>
    <div class="stat" style="left:246px">
      <svg width="130" height="130" viewBox="0 0 130 130" aria-hidden="true">
        <circle cx="65" cy="65" r="60" fill="none" stroke="var(--teal)" stroke-width="5" stroke-dasharray="282.7 377" transform="rotate(-90 65 65)"/>
      </svg>
      <div class="stat__value">75%</div>
      <div class="stat__label">Lorem</div>
    </div>
    <div class="stat" style="left:464px">
      <svg width="130" height="130" viewBox="0 0 130 130" aria-hidden="true">
        <circle cx="65" cy="65" r="60" fill="none" stroke="var(--teal)" stroke-width="5" stroke-dasharray="94.2 377" transform="rotate(-90 65 65)"/>
      </svg>
      <div class="stat__value">25%</div>
      <div class="stat__label">Ipsum</div>
    </div>
  </section>

  <article class="article">
    <h2 class="article__title">Advantages of Virtualization and it’s Role in The Technology World</h2>
    <h3 class="article__sub">Efficiency</h3>
    <p>Praesent id elementum leo, et tristique ante. Duis egestas in ipsum at molestie. Pellentesque neque risus, iaculis ut consequat id, tristique eget libero. Etiam vel lorem condimentum, lacinia magna ornare, faucibus odio. Vivamus nec facilisis eros. Mauris pharetra dolor a neque lobortis aliquet. Suspendisse vitae ultrices sem. Donec eleifend porta eros at dictum. Pellentesque interdum non orci vel placerat. Nam varius ultrices quam non pharetra. Donec in nisl luctus est molestie imperdiet.</p>
    <h3 class="article__sub">Cost</h3>
    <p>Nulla nec rhoncus lorem, et tristique nulla. Maecenas viverra est et turpis consequat dapibus. Sed sapien ipsum, ultrices a sollicitudin vitae, cursus id ligula. Etiam pulvinar porttitor metus non eleifend. Nunc gravida justo nunc, sed ullamcorper ex interdum blandit. Aliquam sed sem metus. Aliquam porttitor nisl in aliquam ultricies. Integer eget est volutpat, dignissim diam in, vehicula erat. Aenean eleifend arcu eu ante laoreet scelerisque. Cras quis ornare urna.</p>
    <h3 class="article__sub">TCO Reduction</h3>
    <p>Nullam et turpis semper, aliquet purus ac, malesuada dolor. Donec id convallis turpis. Nunc metus ligula, volutpat in turpis eget, porta consectetur felis.Aliquam efficitur leo pharetra pretium dictum. Aenean pellentesque ullamcorper dui, at egest.</p>
    <h3 class="article__conclusion">Conclusion</h3>
    <p>Proin id dui vel sem maximus molestie at ut magna. Nunc blandit justo in quam fringilla placerat at quis est. Nulla eu turpis ut lorem varius imperdiet sed vel orci. Fusce gravida ipsum a hendrerit suscipit. Quisque condimentum egestas lacus a rutrum. Integer pulvinar a lectus ut faucibus. Proin aliquet leo in nunc tincidunt gravida.</p>
    <p class="read-more">Read more at <a href="http://leafnote.io/e-1463805925">http://leafnote.io/e-1463805925</a></p>
  </article>

  <footer class="page-tag">Brightwell Systems Partners &nbsp;|&nbsp; 1</footer>
</div>
</body>
</html>
```